Banner Ad Design Project

We need a 728x90 and a 300x250
1st option
"I have a lead for you. Click here to close the deal."
In large bold letters.
Under this in smaller letters,
"Brindlow. For serious business networkers"
2nd option
"Put that coffee down!"
"Coffee's for closers only."
Close more deals. BRINDLOW LOGO
(this is a quote from Harrowmere Standoff. It is a famous sales movie)
The other option is
"First you get the money" "Then you get the power" in bold letters.
"Brindlow. For serious business networkers" in smaller letters at the bottom.
-Must have our colors
-Must have our logo (Small at the bottom right)
-Watch the video at brindlow () com
Please be creative. If the banner can have multiple images that would be great as well.
This needs to be a serious looking ad that is bold and clean.
Updates
Please be sure to use the phrase, "Put that coffee down! Coffee's for closers only" with the logo and at the bottom the words, Brindlow, for serious business networkers. in one of the designs. This will be our first campaign. I am looking for a very simple design that is bold. Perhaps just a coffee cup with the words and no other graphics.
Target Market(s)
Sales professionals
Industry/Entity Type
Business
Look and feel
Each slider illustrates characteristics of the customer's brand and the style your logo design should communicate.

```html
<!DOCTYPE html>
<html lang="en">
<head>
<meta charset="utf-8">
<title>Brindlow Banner Ads</title>
<link href="https://fonts.googleapis.com/css2?family=Source+Sans+3:wght@400;600&display=swap" rel="stylesheet">
<style>
  :root {
    --brand-blue: #34569a;
    --brand-green: #5aa63a;
    --brand-orange: #f3a21d;
    --paper: #ffffff;
    --canvas: #ffffff;
    --shadow: rgba(0, 0, 0, 0.45);
  }
  html, body {
    margin: 0;
    padding: 0;
    overflow: hidden;
  }
  body {
    width: 1200px;
    height: 1000px;
    background: var(--canvas);
    position: relative;
    font-family: "Source Sans 3", "Myriad Pro", sans-serif;
  }
  .banner {
    position: absolute;
    background: var(--paper);
    box-shadow: 4px 6px 10px var(--shadow);
  }
  .banner--leaderboard {
    left: 50px;
    width: 1056px;
    height: 130px;
  }
  .banner--lead { top: 90px; }
  .banner--money { top: 295px; width: 1058px; }

  .brand-mark {
    position: absolute;
    left: 18px;
    top: 14px;
    width: 88px;
    display: flex;
    flex-direction: column;
    align-items: center;
    gap: 6px;
  }
  .brand-mark__square {
    width: 52px;
    height: 52px;
    background: var(--brand-blue);
    border-radius: 6px;
  }
  .brand-mark__name {
    color: var(--brand-blue);
    font-size: 16px;
    font-weight: 400;
    line-height: 1;
  }

  .headline {
    position: absolute;
    left: 105px;
    right: 0;
    top: 14px;
    margin: 0;
    text-align: center;
    color: var(--brand-blue);
    font-weight: 400;
    font-size: 41px;
    line-height: 52px;
    white-space: nowrap;
  }
  .banner--money .headline { left: 100px; font-size: 40px; }
  .tagline {
    position: absolute;
    left: 105px;
    right: 0;
    top: 76px;
    margin: 0;
    text-align: center;
    color: var(--brand-blue);
    font-size: 23px;
    font-weight: 400;
    line-height: 30px;
  }

  .banner--rectangle {
    left: 343px;
    top: 495px;
    width: 522px;
    height: 435px;
  }
  .bubbles {
    position: absolute;
    inset: 0;
  }
  .bubble-text {
    position: absolute;
    margin: 0;
    color: var(--paper);
    text-align: center;
    font-weight: 400;
    white-space: nowrap;
  }
  .bubble-text--command {
    left: 33px;
    width: 399px;
    top: 58px;
    font-size: 37px;
    line-height: 44px;
  }
  .bubble-text--closers {
    left: 33px;
    width: 299px;
    top: 322px;
    font-size: 21px;
    line-height: 28px;
  }
  .rect-brand {
    position: absolute;
    left: 280px;
    top: 178px;
    display: flex;
    align-items: center;
    gap: 12px;
  }
  .rect-brand__square {
    width: 56px;
    height: 56px;
    background: var(--brand-blue);
    border-radius: 6px;
  }
  .rect-brand__name {
    color: var(--brand-blue);
    font-size: 40px;
    font-weight: 400;
    line-height: 1;
  }
</style>
</head>
<body>

  <section class="banner banner--leaderboard banner--lead">
    <div class="brand-mark">
      <span class="brand-mark__square"></span>
      <span class="brand-mark__name">Brindlow</span>
    </div>
    <h1 class="headline">"I have a lead for you. Click here to close the deal"</h1>
    <p class="tagline">"Brindlow. For serious business networkers"</p>
  </section>

  <section class="banner banner--leaderboard banner--money">
    <div class="brand-mark">
      <span class="brand-mark__square"></span>
      <span class="brand-mark__name">Brindlow</span>
    </div>
    <h1 class="headline">"First you get the money - Then you get the power"</h1>
    <p class="tagline">"Brindlow. For serious business networkers"</p>
  </section>

  <section class="banner banner--rectangle">
    <svg class="bubbles" width="522" height="435" viewBox="0 0 522 435" aria-hidden="true">
      <rect x="33" y="28" width="399" height="105" rx="8" fill="var(--brand-green)"/>
      <polygon points="80,130 112,130 36,200" fill="var(--brand-green)"/>
      <rect x="33" y="297" width="299" height="78" rx="6" fill="var(--brand-green)"/>
      <polygon points="62,372 92,372 36,425" fill="var(--brand-green)"/>
    </svg>
    <p class="bubble-text bubble-text--command">"Put that coffee down!"</p>
    <div class="rect-brand">
      <span class="rect-brand__square"></span>
      <span class="rect-brand__name">Brindlow</span>
    </div>
    <p class="bubble-text bubble-text--closers">"Coffee's for closers only."</p>
  </section>

</body>
</html>
```